Brightpath Health Flyer Design for Virtual Online Clinic. -5.5 x 8.5 inches (half sheet)

We need a clean, modern flyer design for Brightpath Health, a new virtual walk-in clinic based in British Columbia. The flyer will be used in libraries, pharmacies, and community centers to help residents easily access primary care through their Brightpath Health NFC access card.
The flyer will ask a question : NEED A DOCTOR? This should be large and attention grabbing.
The design should clearly feature a Brightpath Health card image (the access card) as the centerpiece and visually show how patients can use it to book appointments. The tone should feel trustworthy, healthcare-oriented, and community-friendly — clean fonts, clear spacing, and strong readability from a distance.

Side One: This card has the NFC Access Card.
NEED A DOCTOR? (Large Font, Attention Grabbing)
How to Book an Appointment using your Brightpath Health Card
Step 1: Tap Your Card on Your Phone
Hold your card near the back of your phone.
It will activate automatically — no app needed.
The Brightpath Health scheduler will open.
Step 2: Schedule Your Appointment
Select your clinical concern.
Choose your time window.
Register (only once).
Confirm your appointment.
Step 3: Relax, we’ll take care of the rest
A doctor will call during your scheduled time.
Once booked, you’ll be able to call our office.
No emails, no texts — just a real person.
It’s that simple.
Side Two:
About Brightpath Health
Created by Dr. Marcus Feldtree
Brightpath Health was founded to make healthcare simple and convenient. Prescription renewals. Common infections. Medical notes. And so much more.
Our doctors can address 120+ health concerns virtually — providing quality care without the waiting room. No waiting rooms. Just real doctors providing real care.
Why Patients Choose Brightpath Health
Easy access – book and be seen from anywhere in BC.
Effortless booking – tap your Brightpath Health Card to begin.
Trusted physicians – every visit is with a licensed BC family doctor.
How It Works
Book your visit — choose a time window that fits your day.
Join the queue — you’ll be called when it’s your turn.
Speak directly with your doctor — simple, secure, and stress-free.
Convenient Care for Common Concerns

Additional Details.
Please find the domain to be launched soon. I've attached the NFC card file for review, it is 85.5 mm x 54 mm. The card will be glued to the flyer.
I've attached examples of flyers but they are not the look I am seeking and I am looking for creative solutions.
Thank you!
http://brightpath-example.test/

Target Market(s)

Adult Patients in British Columbia

Industry/Entity Type

Healthcare

Font styles to use
Other font styles liked:
• Looking for clean lines, uniform appearance, and high legibility i.e poppins

Colors
0054AA
0677BA
7BADD7
CADEEF
E8F1F8

Requirements
Must have
• Need A Doctor?
Nice to have
• Elegant style, not too busy, clear layout.
Should not have
• Clutter, look cheap - review examples.

```html
<!DOCTYPE html>
<html lang="en">
<head>
<meta charset="utf-8">
<title>Brightpath Health – Flyer Spread</title>
<link href="https://fonts.googleapis.com/css2?family=Poppins:wght@400;500&family=Great+Vibes&family=Oswald:wght@400&display=swap" rel="stylesheet">
<style>
  :root{
    --blue:#0054AA;
    --blue-deep:#0A4FA6;
    --blue-number:rgba(0,40,110,.35);
    --ink:#111;
    --black:#000;
    --white:#fff;
    --paper:#fff;
  }
  *{box-sizing:border-box;margin:0;padding:0}
  html,body{width:1200px;height:926px;overflow:hidden;background:var(--paper)}
  body{position:relative;font-family:'Poppins',sans-serif;color:var(--ink)}
  .page{position:absolute;top:52px;width:532px;height:822px;overflow:hidden;background:var(--white)}
  .page--front{left:49px}
  .page--back{left:618px}
  .page-shapes{position:absolute;inset:0;width:532px;height:822px}
  .abs{position:absolute}

  .headline{left:0;width:532px;top:220px;text-align:center;font-family:'Oswald',sans-serif;font-weight:400;
    font-size:48px;line-height:52px;color:var(--white);letter-spacing:.5px}
  .headline span{display:block}
  .headline .l1{transform:translateX(-4px)}
  .brand-mark{left:22px;top:380px;font-size:20px;font-weight:500;color:var(--blue)}

  .script{font-family:'Great Vibes',cursive;font-weight:400;line-height:1}
  .book-title{left:0;width:532px;top:508px;text-align:center;color:var(--white);font-size:29px}
  .book-title span{display:block;margin-bottom:12px}

  .step-divider{width:1px;top:601px;height:220px;background:rgba(255,255,255,.22)}
  .step{top:607px;width:165px;color:var(--white)}
  .step-icon{width:40px;height:40px;display:block}
  .step-number{top:607px;font-size:42px;font-weight:500;color:var(--blue-number);line-height:40px}
  .step-title{margin-top:16px;font-size:10.5px;font-weight:500;letter-spacing:.3px;line-height:22px;text-transform:uppercase}
  .step-body{margin-top:11px;font-size:9.6px;line-height:19.3px}

  .access-card{width:174px;height:92px;border-radius:9px;background:var(--white);overflow:hidden;
    box-shadow:0 1px 4px rgba(0,0,0,.25)}
  .access-card svg{position:absolute;left:0;top:0}
  .access-card .card-name{position:absolute;left:60px;top:37px;font-size:11.5px;font-weight:500;color:var(--blue)}
  .access-card .card-tap{position:absolute;right:26px;bottom:10px;font-size:5px;color:var(--blue)}
  .access-card .card-chip{position:absolute;right:12px;bottom:9px;width:12px;height:8px;border:1px solid var(--blue);border-radius:2px}

  .why-title{left:25px;top:156px;color:var(--white);font-size:29px}
  .why-title span{display:block;margin-bottom:14px}
  .feature{left:22px;width:258px}
  .feature-icon{position:absolute;left:3px;top:2px;width:26px;height:36px}
  .feature-title{margin-left:55px;font-size:10.5px;font-weight:500;letter-spacing:.3px;color:var(--white)}
  .feature-body{margin-left:55px;margin-top:14px;font-size:9.8px;line-height:19px;color:var(--white)}
  .feature-rule{left:22px;width:257px;height:1px;background:rgba(255,255,255,.25)}

  .about-title{left:328px;top:265px;color:var(--white);font-size:27px}
  .about-title span{display:block;margin-bottom:16px}
  .about-body{left:328px;top:366px;width:178px;font-size:10.2px;line-height:23.2px;color:var(--white)}

  .works-title{left:16px;top:632px;color:var(--blue);font-size:31px}
  .works-divider{width:1px;top:681px;height:107px;background:#d6d6d6}
  .work{top:684px}
  .work-icon{width:34px;height:32px;display:block}
  .work-title{margin-top:20px;font-size:10px;font-weight:500;letter-spacing:.3px;line-height:18px;color:var(--blue);text-transform:uppercase}
  .work-body{margin-top:6px;font-size:9.6px;line-height:19px;color:var(--ink)}
  .tagline{left:25px;top:803px;font-size:9.8px;color:var(--ink)}
</style>
</head>
<body>

<!-- FRONT -->
<section class="page page--front">
  <svg class="page-shapes" viewBox="0 0 969 1496" preserveAspectRatio="none">
    <defs>
      <linearGradient id="clinicPhoto" x1="0" y1="0" x2="1" y2="1">
        <stop offset="0" stop-color="#c9d3dc"/>
        <stop offset=".45" stop-color="#8fa3b6"/>
        <stop offset="1" stop-color="#3f4f61"/>
      </linearGradient>
    </defs>
    <g role="img" aria-label="Photo of a doctor using a monitor in a bright modern hospital room with a nurse by a bed">
      <polygon points="0,0 969,0 969,565 722,655 722,700 0,940" fill="url(#clinicPhoto)"/>
    </g>
    <polygon points="310,0 385,0 969,258 969,232" fill="var(--white)"/>
    <polygon points="385,0 969,0 969,232" fill="var(--blue)"/>
    <polygon points="0,475 540,680 0,938" fill="var(--white)"/>
    <polygon points="255,340 722,340 722,700 0,938 540,680 255,572" fill="var(--black)" fill-opacity=".9"/>
    <polygon points="0,940 722,700 722,655 969,565 969,1496 0,1496" fill="var(--blue)"/>
  </svg>

  <h1 class="abs headline"><span class="l1">NEED&nbsp; A</span><span>DOCTOR?</span></h1>
  <div class="abs brand-mark">Brightpath Health</div>

  <div class="abs access-card" style="left:333px;top:400px">
    <svg width="174" height="92" viewBox="0 0 174 92"><path d="M0 0H62C50 20 44 40 42 55C40 70 36 80 38 92H0Z" fill="var(--blue-deep)"/></svg>
    <span class="card-name">Brightpath Health</span>
    <span class="card-tap">Tap Here to Book</span>
    <span class="card-chip"></span>
  </div>

  <h2 class="abs script book-title"><span>How to Book an Appointment using your</span><span>Brightpath Health Card</span></h2>

  <div class="abs step-divider" style="left:180px"></div>
  <div class="abs step-divider" style="left:347px"></div>

  <div class="abs step-number" style="left:114px">01</div>
  <div class="abs step-number" style="left:283px">02</div>
  <div class="abs step-number" style="left:464px">03</div>

  <article class="abs step" style="left:21px">
    <svg class="step-icon" viewBox="0 0 40 40" fill="none" stroke="#fff" stroke-width="1.5">
      <path d="M3 9a10 10 0 0 1 16 0M6 12a6 6 0 0 1 10 0M9 15a2 2 0 0 1 4 0"/>
      <rect x="6" y="18" width="22" height="14" rx="2"/><path d="M6 22h22"/>
      <rect x="24" y="20" width="12" height="18" rx="2"/>
    </svg>
    <h3 class="step-title">Tap your card on your<br>phone</h3>
    <p class="step-body">Hold your card near the back of your phone. It will activate automatically — no app needed. The Brightpath Health scheduler will open.</p>
  </article>

  <article class="abs step" style="left:200px;width:140px">
    <svg class="step-icon" viewBox="0 0 40 40" fill="none" stroke="#fff" stroke-width="1.5">
      <rect x="2" y="5" width="30" height="28" rx="2"/><path d="M2 11h30M8 2v6M26 2v6"/>
      <path d="M7 16h4M14 16h4M21 16h4M7 22h4M14 22h4M7 28h4"/>
      <circle cx="31" cy="30" r="7" fill="var(--blue)"/><path d="M31 26v4h3"/>
    </svg>
    <h3 class="step-title">Schedule your<br>appointment</h3>
    <p class="step-body">Select your clinical concern. Choose your time window. Register (only once). Confirm your appointment.</p>
  </article>

  <article class="abs step" style="left:383px;width:140px">
    <svg class="step-icon" viewBox="0 0 40 40" fill="none" stroke="#fff" stroke-width="1.5">
      <circle cx="20" cy="16" r="7"/><path d="M16 17q4 3 8 0"/>
      <path d="M8 36q0-10 12-10t12 10Z"/><path d="M20 2v3M10 6l2 2M30 6l-2 2M5 14h3M32 14h3"/>
    </svg>
    <h3 class="step-title">Relax, we’ll take<br>care of the rest</h3>
    <p class="step-body">A doctor will call during your scheduled time. Once booked, you’ll be able to call our office. No emails, no texts — just a real person.</p>
  </article>
</section>

<!-- BACK -->
<section class="page page--back">
  <svg class="page-shapes" viewBox="0 0 969 1496" preserveAspectRatio="none">
    <defs>
      <linearGradient id="consultPhoto" x1="0" y1="0" x2="1" y2="0">
        <stop offset="0" stop-color="#8a7a6a"/>
        <stop offset=".4" stop-color="#c9cfc8"/>
        <stop offset="1" stop-color="#dfe3e2"/>
      </linearGradient>
    </defs>
    <g role="img" aria-label="Photo of a patient on a video consultation with a doctor shown on a desktop monitor">
      <polygon points="0,0 969,0 969,470 0,105" fill="url(#consultPhoto)"/>
    </g>
    <polygon points="548,338 969,495 969,1390 173,1012 548,920" fill="var(--blue)"/>
    <polygon points="0,125 548,335 548,920 0,1055" fill="var(--black)"/>
    <polygon points="0,118 548,328 548,338 0,128" fill="var(--blue)"/>
  </svg>

  <h2 class="abs script why-title"><span>Why Patients</span><span>Choose Brightpath Health</span></h2>

  <div class="abs feature" style="top:264px">
    <svg class="feature-icon" viewBox="0 0 26 36" fill="none" stroke="#fff" stroke-width="1.3">
      <rect x="1" y="4" width="18" height="5"/><rect x="1" y="11" width="18" height="5"/><rect x="1" y="18" width="14" height="5"/><rect x="1" y="25" width="12" height="5"/>
      <circle cx="19" cy="26" r="7"/><path d="M16 26a3 3 0 0 1 6 0M18 29a1 1 0 0 1 2-3"/>
    </svg>
    <div class="feature-title">EASY ACCESS</div>
    <div class="feature-body">Book and be seen from anywhere in BC.</div>
  </div>
  <div class="abs feature-rule" style="top:328px"></div>

  <div class="abs feature" style="top:351px">
    <svg class="feature-icon" viewBox="0 0 26 36" fill="none" stroke="#fff" stroke-width="1.3">
      <rect x="2" y="2" width="16" height="28" rx="2"/><circle cx="10" cy="11" r="4"/><path d="M8 11l2 2 3-4"/>
      <path d="M13 34v-9a2 2 0 0 1 4 0v5l5 1v4"/>
    </svg>
    <div class="feature-title">EFFORTLESS BOOKING</div>
    <div class="feature-body">Tap your Brightpath Health Card to begin.</div>
  </div>
  <div class="abs feature-rule" style="top:418px"></div>

  <div class="abs feature" style="top:438px">
    <svg class="feature-icon" viewBox="0 0 26 36" fill="none" stroke="#fff" stroke-width="1.3">
      <circle cx="13" cy="10" r="6"/><path d="M7 8h12"/><path d="M1 34q0-12 12-12t12 12Z"/><path d="M9 24v5a2 2 0 0 0 4 0M17 24v4"/>
    </svg>
    <div class="feature-title">TRUSTED PHYSICIANS</div>
    <div class="feature-body">Every visit is with a licensed BC family doctor.</div>
  </div>

  <div class="abs access-card" style="left:58px;top:519px">
    <svg width="174" height="92" viewBox="0 0 174 92"><path d="M0 0H62C50 20 44 40 42 55C40 70 36 80 38 92H0Z" fill="var(--blue-deep)"/></svg>
    <span class="card-name">Brightpath Health</span>
    <span class="card-tap">Tap Here to Book</span>
    <span class="card-chip"></span>
  </div>

  <h2 class="abs script about-title"><span>About</span><span>Brightpath Health</span></h2>
  <p class="abs about-body">Created by Dr. Marcus Feldtree Brightpath Health was founded to make healthcare simple and convenient. Prescription renewals. Common infections. Medical notes. And so much more. Our doctors can address 120+ health concerns virtually — providing quality care without the waiting room. No waiting rooms. Just real doctors providing real care.</p>

  <h2 class="abs script works-title">How It Works</h2>
  <div class="abs works-divider" style="left:173px"></div>
  <div class="abs works-divider" style="left:309px"></div>

  <article class="abs work" style="left:25px;width:140px">
    <svg class="work-icon" viewBox="0 0 34 32" fill="none" stroke="var(--blue)" stroke-width="1.3">
      <rect x="1" y="16" width="18" height="14"/><path d="M10 19v8M6 23h8"/><circle cx="26" cy="8" r="4"/><path d="M22 30V15h8v15"/><rect x="5" y="3" width="10" height="8"/>
    </svg>
    <h3 class="work-title">Book your visit</h3>
    <p class="work-body">Choose a time window that fits your day.</p>
  </article>

  <article class="abs work" style="left:191px;width:112px">
    <svg class="work-icon" viewBox="0 0 34 32" fill="none" stroke="var(--blue)" stroke-width="1.3">
      <path d="M2 4h6M6 2l2 2-2 2M24 4h6M28 2l2 2-2 2"/>
      <circle cx="6" cy="14" r="2"/><circle cx="13" cy="12" r="2"/><circle cx="20" cy="14" r="2"/><circle cx="27" cy="12" r="2"/>
      <path d="M4 30V18h4v12M11 30V16h4v14M18 30V18h4v12M25 30V16h4v14"/>
    </svg>
    <h3 class="work-title">Join the queue</h3>
    <p class="work-body">You’ll be called when it’s your turn.</p>
  </article>

  <article class="abs work" style="left:337px;width:170px">
    <svg class="work-icon" viewBox="0 0 34 32" fill="none" stroke="var(--blue)" stroke-width="1.3">
      <rect x="14" y="2" width="18" height="12" rx="2"/><path d="M18 14l-3 4v-4"/><circle cx="10" cy="14" r="5"/><path d="M2 31q0-10 8-10t8 10"/>
    </svg>
    <h3 class="work-title">Speak directly with<br>your doctor</h3>
    <p class="work-body">Simple, secure, and stress-free.</p>
  </article>

  <p class="abs tagline">Convenient Care for Common Concerns</p>
</section>

</body>
</html>
```